PebbleLoop screens tidy up

We would like advice on how to better present the following home page and overview pages.

The existing website is functional, but the pages don't appear professionals and pleasing to the eye. We would specifically like feedback on alignment and padding of icons and text to make the screen more appealing and polished.

We are following the quartz design system.

Number of Pages Required

1 page

Font styles to use
Sans Serif
Other font styles liked:
• IBM Plex, Poppins

```html
<!DOCTYPE html>
<html lang="en">
<head>
<meta charset="utf-8">
<title>PebbleLoop – Home</title>
<link rel="stylesheet" href="https://fonts.googleapis.com/css2?family=Inter:wght@400;500;600&display=swap">
<style>
  :root{
    --ink:#1d1f24;
    --ink-soft:#3a3d44;
    --muted:#9a9ea6;
    --line:#e3e6ea;
    --surface:#ffffff;
    --canvas:#e9eef3;
    --accent:#f2a03d;
    --nav-active:#f1f2f4;
  }
  *{box-sizing:border-box;margin:0;padding:0}
  html,body{width:1200px;height:853px;overflow:hidden}
  body{font-family:"Inter",sans-serif;color:var(--ink);background:var(--canvas);position:relative}

  .sidebar{position:absolute;left:0;top:0;width:218px;height:853px;background:var(--surface);border-right:1px solid var(--line)}
  .brand{position:absolute;left:15px;top:18px;display:flex;align-items:center;gap:8px}
  .brand-mark{width:30px;height:30px;border-radius:50%;background:var(--accent)}
  .brand-name{font-size:20px;font-weight:600;color:var(--ink-soft);letter-spacing:-.3px}

  .nav-item{position:absolute;left:13px;width:192px;height:23px;display:flex;align-items:center;gap:6px;padding-left:8px;font-size:12px;color:var(--ink)}
  .nav-item svg{width:14px;height:14px;stroke:var(--ink);fill:none;stroke-width:1.3}
  .nav-item.is-active{background:var(--nav-active);border-radius:3px}
  .nav-item.is-active::before{content:"";position:absolute;left:0;top:4px;width:3px;height:15px;background:var(--accent);border-radius:2px}

  .section-title{position:absolute;left:13px;top:179px;font-size:12px;font-weight:600}
  .section-add{position:absolute;left:190px;top:180px;width:14px;height:14px;stroke:var(--ink);stroke-width:1.3}

  .tree-row{position:absolute;left:15px;display:flex;align-items:center;font-size:12px;height:20px}
  .tree-row .chev{width:8px;height:8px;stroke:#b5b8be;fill:none;stroke-width:1.2;margin-right:8px}
  .tree-row .doc{width:13px;height:13px;stroke:var(--ink);fill:none;stroke-width:1.1;margin-right:6px}
  .tree-sub{position:absolute;left:50px;font-size:12px}

  .topbar{position:absolute;left:218px;top:0;width:982px;height:60px;background:var(--surface);border-bottom:1px solid var(--line)}
  .crumb{position:absolute;left:31px;top:23px;font-size:12px}
  .search{position:absolute;left:659px;top:18px;width:133px;height:23px;background:#f3f4f6;border-radius:3px;display:flex;align-items:center;gap:5px;padding-left:8px;font-size:11px;color:#b7bac0}
  .search svg{width:11px;height:11px;stroke:#b7bac0;fill:none;stroke-width:1.3}
  .user{position:absolute;left:812px;top:20px;display:flex;align-items:center;gap:7px;font-size:12px}
  .avatar{width:20px;height:20px;border-radius:50%;background:linear-gradient(135deg,#6b6f76,#2c2e33)}
  .user-chev{position:absolute;left:948px;top:27px;width:9px;height:6px;stroke:#b5b8be;fill:none;stroke-width:1.2}

  .label{position:absolute;font-size:12px;font-weight:600}
  .card{position:absolute;background:var(--surface);border-radius:8px}
  .team-name{position:absolute;left:20px;top:26px;font-size:20px;font-weight:600}
  .team-desc{position:absolute;left:20px;top:58px;font-size:12px;color:var(--muted)}

  .usage-title{position:absolute;left:20px;top:22px;font-size:10px;color:var(--ink-soft)}
  .usage-bar{position:absolute;left:20px;top:40px;width:416px;height:1px;background:#d7dade}
  .usage-bar::before{content:"";position:absolute;left:0;top:-.5px;width:8px;height:2px;background:var(--accent)}
  .usage-note{position:absolute;left:20px;top:48px;font-size:9.5px;color:var(--muted)}

  .stat-title{position:absolute;left:20px;top:29px;font-size:12px;font-weight:600}
  .stat-value{position:absolute;left:20px;top:53px;font-size:20px;font-weight:500;color:var(--accent)}

  .btn-new{position:absolute;left:1055px;top:380px;width:122px;height:30px;background:var(--accent);border-radius:4px;color:#fff;font-size:10px;font-weight:500;display:flex;align-items:center;justify-content:center;gap:6px}
  .btn-new svg{width:12px;height:12px;stroke:#fff;stroke-width:1.4}

  .campaign{top:420px;width:304px;height:143px}
  .campaign h3{position:absolute;left:20px;top:24px;font-size:12px;font-weight:600}
  .campaign .more{position:absolute;right:25px;top:31px;width:12px;height:3px;fill:var(--ink)}
  .campaign .desc{position:absolute;left:20px;top:52px;font-size:10px;color:var(--muted)}
  .campaign .count{position:absolute;left:20px;top:75px;font-size:18px;color:var(--accent)}
  .campaign .state{position:absolute;left:41px;top:74px;font-size:9.5px;color:var(--muted);line-height:1}
  .campaign .kind{position:absolute;left:41px;top:85px;font-size:12px;font-weight:500}
  .campaign .since{position:absolute;left:20px;top:110px;font-size:10px;color:var(--muted)}
</style>
</head>
<body>

<aside class="sidebar">
  <div class="brand"><span class="brand-mark"></span><span class="brand-name">PebbleLoop</span></div>

  <div class="nav-item is-active" style="top:76px">
    <svg viewBox="0 0 14 14"><circle cx="7" cy="7" r="6"/><path d="M7 1v6h6M7 7l-4 4.5"/></svg>Home
  </div>
  <div class="nav-item" style="top:102px">
    <svg viewBox="0 0 14 14"><path d="M3 10V6a4 4 0 0 1 8 0v4l1 1H2zM5.5 12.5h3"/></svg>All Alerts
  </div>
  <div class="nav-item" style="top:129px">
    <svg viewBox="0 0 14 14"><circle cx="7" cy="7" r="2"/><path d="M7 1l1.3 1.6 2-.3.4 2 1.8 1-.9 1.7.9 1.7-1.8 1-.4 2-2-.3L7 13l-1.3-1.6-2 .3-.4-2-1.8-1L2.4 7l-.9-1.7 1.8-1 .4-2 2 .3z"/></svg>Manage
  </div>

  <div class="section-title">Campaigns</div>
  <svg class="section-add" viewBox="0 0 14 14"><path d="M7 1v12M1 7h12"/></svg>

  <div class="tree-row" style="top:204px">
    <svg class="chev" viewBox="0 0 8 8"><path d="M1 2.5l3 3 3-3"/></svg>
    <svg class="doc" viewBox="0 0 13 13"><rect x="1" y="1" width="11" height="11"/><path d="M4 1v11M6 4h4M6 6.5h4M6 9h4"/></svg>My Custom Campaign
  </div>
  <div class="tree-sub" style="top:233px">Overview</div>
  <div class="tree-sub" style="top:260px">Files &amp; Honey Tokens</div>
  <div class="tree-sub" style="top:286px">Resources</div>
  <div class="tree-sub" style="top:313px">Alerts</div>
  <div class="tree-sub" style="top:340px">Settings</div>
  <div class="tree-row" style="top:364px">
    <svg class="chev" viewBox="0 0 8 8"><path d="M2.5 1l3 3-3 3"/></svg>
    <svg class="doc" viewBox="0 0 13 13"><rect x="1" y="1" width="11" height="11"/><path d="M4 1v11M6 4h4M6 6.5h4M6 9h4"/></svg>Default Campaign
  </div>
</aside>

<header class="topbar">
  <div class="crumb">Home</div>
  <div class="search"><svg viewBox="0 0 11 11"><circle cx="4.5" cy="4.5" r="3.5"/><path d="M7 7l3 3"/></svg>Search</div>
  <div class="user"><span class="avatar" role="img" aria-label="User profile photo"></span>Mara Velt</div>
  <svg class="user-chev" viewBox="0 0 9 6"><path d="M1 1l3.5 3.5L8 1"/></svg>
</header>

<main>
  <div class="label" style="left:242px;top:85px">Teamspace</div>
  <section class="card" style="left:242px;top:110px;width:935px;height:93px">
    <div class="team-name">Default</div>
    <div class="team-desc">The default client is created as a part of your user account.</div>
  </section>

  <div class="label" style="left:242px;top:228px">Subscription Overview</div>
  <section class="card" style="left:242px;top:253px;width:455px;height:104px">
    <div class="usage-title">Starter pack usage</div>
    <div class="usage-bar"></div>
    <div class="usage-note">0 files active out of 10 allowed</div>
  </section>

  <div class="label" style="left:721px;top:228px">Files &amp; Honey Tokens</div>
  <section class="card" style="left:721px;top:253px;width:222px;height:107px">
    <div class="stat-title">Files</div>
    <div class="stat-value">0</div>
  </section>
  <section class="card" style="left:954px;top:253px;width:223px;height:107px">
    <div class="stat-title">Honey Tokens</div>
    <div class="stat-value">30</div>
  </section>

  <div class="label" style="left:242px;top:388px">Campaigns</div>
  <div class="btn-new">New Campaign <svg viewBox="0 0 12 12"><path d="M6 0v12M0 6h12"/></svg></div>

  <article class="card campaign" style="left:242px">
    <h3>My Custom Campaign</h3>
    <svg class="more" viewBox="0 0 12 3"><circle cx="1.5" cy="1.5" r="1.2"/><circle cx="6" cy="1.5" r="1.2"/><circle cx="10.5" cy="1.5" r="1.2"/></svg>
    <div class="desc">This is my custom campaign for finding ...</div>
    <div class="count">0</div>
    <div class="state">Active</div>
    <div class="kind">Files and Honey Tokens</div>
    <div class="since">Active since: 25/07/2023 13:12</div>
  </article>
  <article class="card campaign" style="left:557px">
    <h3>Default Campaign</h3>
    <svg class="more" viewBox="0 0 12 3"><circle cx="1.5" cy="1.5" r="1.2"/><circle cx="6" cy="1.5" r="1.2"/><circle cx="10.5" cy="1.5" r="1.2"/></svg>
    <div class="desc">This is my custom campaign for finding ...</div>
    <div class="count">0</div>
    <div class="state">Active</div>
    <div class="kind">Files and Honey Tokens</div>
    <div class="since">Active since: 25/07/2023 13:12</div>
  </article>
  <article class="card campaign" style="left:873px">
    <h3>My Custom Campaign</h3>
    <svg class="more" viewBox="0 0 12 3"><circle cx="1.5" cy="1.5" r="1.2"/><circle cx="6" cy="1.5" r="1.2"/><circle cx="10.5" cy="1.5" r="1.2"/></svg>
    <div class="desc">This is my custom campaign for finding ...</div>
    <div class="count">0</div>
    <div class="state">Active</div>
    <div class="kind">Files and Honey Tokens</div>
    <div class="since">Active since: 25/07/2023 13:12</div>
  </article>
</main>

</body>
</html>
```